Larkfield Clinic Booklet 2016

Larkfield Clinic is a multi-specialty Practice in Midtown Manhattan offering advanced care in multiple areas of medicine. See our table of contents (PDF Uploaded)
Our designed booklet should be clean, easy to read, contemporary, high-end and elegant.
We need a general theme, Layout for cover and templates for internal.
We are entertaining the idea of two different sizes
8 x 10
or
11 x 8.5
Our tagline " The Future of Medicine is Here"
We will provide all the text content
The link to our website
www.LarkfieldCL.example
Uploaded files are as follows.. Logo, Our Team Photo and the PDF listing the table of contents.

```html
<!DOCTYPE html>
<html lang="en">
<head>
<meta charset="utf-8">
<title>Larkfield Clinic Booklet</title>
<link rel="stylesheet" href="https://fonts.googleapis.com/css2?family=Raleway:wght@200;300;400;500;600&display=swap">
<style>
  :root{
    --bg:#e4e5e7;
    --blue:#3e5f8a;
    --blue-deep:#2f4e78;
    --blue-text:#e3e9f1;
    --ink:#3b3f45;
    --muted:#7b8088;
    --grey-band:#bfc1c4;
    --grey-foot:#d9dadc;
    --paper:#ffffff;
    --photo-light:#d9dde2;
    --photo-mid:#a9b3bf;
  }
  *{box-sizing:border-box;margin:0;padding:0}
  html,body{width:1200px;height:785px;overflow:hidden;background:var(--bg)}
  body{font-family:"Raleway",sans-serif;color:var(--ink)}
  .canvas{position:relative;width:1200px;height:785px;overflow:hidden;background:var(--bg)}
  .spread{position:absolute;left:30px;top:40px;width:1140px;height:705px;background:var(--blue);box-shadow:0 6px 18px rgba(0,0,0,.18)}
  .page{position:absolute;top:0;height:705px;overflow:hidden}
  .page-left{left:0;width:460px;background:var(--blue)}
  .page-middle{left:460px;width:370px}
  .top-strip{position:absolute;left:0;top:0;width:100%;height:12px;background:var(--blue-deep)}
  .photo{position:absolute;background:linear-gradient(135deg,var(--photo-light),var(--photo-mid))}
  .page-left .hero-photo{left:0;top:12px;width:460px;height:216px}
  .page-middle .hero-photo{left:0;top:12px;width:370px;height:216px;background:linear-gradient(135deg,#eef0f3,#b7c0cb)}
  .page-copy{position:absolute;font-size:10.5px;line-height:1.6;color:var(--blue-text);text-align:center;font-weight:400}
  .page-copy p{margin-bottom:12px}
  .page-copy p:last-child{margin-bottom:0}
  .title{position:absolute;left:38px;top:236px;font-size:48px;line-height:1;font-weight:200;color:var(--blue-text);letter-spacing:1px}
  .col-a{left:28px;top:302px;width:214px}
  .col-b{left:258px;top:244px;width:188px}
  .inset-photo{left:260px;top:440px;width:184px;height:172px;background:linear-gradient(135deg,#e8ebef,#9aa6b4)}
  .middle-shape{position:absolute;left:0;top:0}
  .col-c{left:22px;top:244px;width:292px}
  .page-flap{left:830px;width:310px;background:var(--paper)}
  .brand{position:absolute;left:24px;top:28px;display:flex;align-items:center;gap:10px}
  .brand-mark{width:26px;height:26px;border-radius:50%;background:var(--blue-deep)}
  .brand-name{font-size:15px;font-weight:500;letter-spacing:1.5px;color:var(--ink);text-transform:uppercase}
  .flap-copy{position:absolute;left:24px;top:82px;width:150px;font-size:10.5px;line-height:1.7;color:var(--muted)}
  .flap-copy p{margin-bottom:12px}
  .services{list-style:none;margin:4px 0 14px}
  .services li{position:relative;padding-left:11px;color:var(--ink);white-space:nowrap}
  .services li::before{content:"";position:absolute;left:0;top:7px;width:4px;height:4px;border-radius:50%;background:var(--blue)}
  .phone-big{font-size:19px;color:var(--blue);font-weight:400;letter-spacing:.5px}
  .team-photo{left:180px;top:372px;width:112px;height:130px;background:linear-gradient(135deg,#f2f3f5,#c6ccd4);border:1px solid #d5d8dc;z-index:1}
  .flap-band{position:absolute;left:0;top:470px;width:310px;height:170px;background:var(--grey-band)}
  .band-accent{position:absolute;right:0;top:78px;width:22px;height:30px;background:var(--blue)}
  .tagline{position:absolute;left:24px;top:40px;font-size:20px;font-weight:300;line-height:1.15;color:var(--paper);letter-spacing:.5px;text-transform:uppercase}
  .signoff{position:absolute;left:24px;top:118px;font-size:10.5px;line-height:1.3;color:var(--paper)}
  .signoff span{display:block;font-size:8.5px;opacity:.85}
  .flap-foot{position:absolute;left:0;top:640px;width:310px;height:65px;background:var(--grey-foot);padding:12px 14px 0;font-size:8.6px;line-height:1.8;color:var(--ink);text-align:right}
  .flap-foot strong{font-weight:600;text-transform:uppercase}
</style>
</head>
<body>
<main class="canvas">
  <section class="spread">

    <article class="page page-left">
      <div class="top-strip"></div>
      <div class="photo hero-photo" role="img" aria-label="Photo of therapists treating patients' back and neck beside a spine scan on a monitor"></div>
      <h1 class="title">We Care</h1>
      <div class="page-copy col-a">
        <p>First thing you should know is that all of our doctors and therapists are experts in their field.</p>
        <p>We literally have everything you need at one location to get better and feel better quickly… all without surgery or other invasive treatments.</p>
        <p>While our staff may include an orthopedic surgeon, we have dedicated ourselves to non-surgical care. That means we do everything to keep you out of surgery… and if you have had surgery…we do everything we can to make sure you have the fastest and most complete recovery you can… so you never need it again.</p>
        <p>I want to tell you how easy it is to get the results you are looking for. It's really just three easy steps. First, you make an appointment to see one of our</p>
      </div>
      <div class="page-copy col-b">
        <p>great doctors. They will sit down with you, one on one, and really listen to your problems. Then… our professional team works together to create a customized treatment plan just for you.</p>
        <p>Here is where the fun part starts! Once we have a plan, we begin the process of getting you to feel better our professional.</p>
      </div>
      <div class="photo inset-photo" role="img" aria-label="Photo of a clinician giving a patient a back injection beside imaging equipment"></div>
    </article>

    <article class="page page-middle">
      <svg class="middle-shape" width="370" height="705" viewBox="0 0 370 705" aria-hidden="true">
        <rect x="0" y="0" width="370" height="705" fill="#ffffff"/>
        <path d="M0 0 H300 C350 200 370 420 340 705 H0 Z" fill="#3e5f8a"/>
        <rect x="0" y="0" width="370" height="12" fill="#2f4e78"/>
      </svg>
      <div class="photo hero-photo" role="img" aria-label="Photo of a doctor performing an ultrasound scan on a patient"></div>
      <div class="page-copy col-c">
        <p>surgery…we do everything we can to make sure you have the fastest and most complete recovery you can… so you never need it again.</p>
        <p>I want to tell you how easy it is to get the results you are looking for. It's really just three easy steps. First, you make an appointment to see one of our great doctors. They will sit down with you, one on one, and really listen to your problems. Then… our professional team works together to create a customized treatment plan just for you our professional.</p>
        <p>Here is where the fun part starts! Once we have a plan, we begin the process of getting you to feel better.</p>
        <p>This is where we excel. Our unique treatment programs are designed to get results faster by combining the best of each speciality.</p>
        <p>The result is we can keep you feeling good for years to come… Again, we can start the process of helping you achieve the health and vitality that you deserve.</p>
      </div>
    </article>

    <aside class="page page-flap">
      <div class="brand">
        <span class="brand-mark"></span>
        <span class="brand-name">Larkfield Clinic</span>
      </div>
      <div class="flap-copy">
        <p>We take great pride in providing the finest medical care to each and every patient.</p>
        <p>The different services offered in our New York office.</p>
        <ul class="services">
          <li>Orthopedics</li>
          <li>Pain Management</li>
          <li>Chiropractic Care</li>
          <li>Physical Therapy</li>
          <li>Acupuncture</li>
          <li>Integrative Medicine</li>
          <li>Platelet Rich Plasma (PRP)</li>
          <li>Advance Knee Care</li>
          <li>Stem Cell Injections</li>
        </ul>
        <p>Please call us at<br><span class="phone-big">555-014-2700</span><br>if you have any questions!</p>
      </div>
      <div class="photo team-photo" role="img" aria-label="Portrait photo of the clinic director in a white coat"></div>
      <div class="flap-band">
        <span class="band-accent"></span>
        <p class="tagline">The Future<br>of Medicine<br>is Here</p>
        <p class="signoff">Dr. Evan Holt,<span>Clinic Director</span></p>
      </div>
      <footer class="flap-foot">
        <strong>Larkfield Clinic</strong> | 48 Alder Street | New York, NY 10099<br>
        www.LarkfieldCL.example<br>
        Phone: 555-014-2700 | Fax: 555-014-2790
      </footer>
    </aside>

  </section>
</main>
</body>
</html>
```